Hargrove Orthopedics and Sports Medicine
Arthroscopy of the Knee and Shoulder
Hargrove Orthopedics and Sports Medicine -
Creative Brief
Cutting-Edge
Daniel K. Hargrove Jr., M.D.
418 North Pelham Street Lowell, AR 72819
quillmoth@mailvane.com
hargrovemd.com
under web address please add fb.com/hargrovemd Do not put email on the card
use large pic of logo or use another idea if you like

```html
<!DOCTYPE html>
<html lang="en">
<head>
<meta charset="utf-8">
<title>Hargrove Orthopedics and Sports Medicine — Stationery</title>
<link href="https://fonts.googleapis.com/css2?family=Open+Sans:wght@400;600;700&display=swap" rel="stylesheet">
<style>
  :root {
    --bg: #e7e4df;
    --paper: #ffffff;
    --navy: #1b3a7a;
    --blue: #2c5fb3;
    --blue-light: #6d95d6;
    --grey-flap: #8a8f96;
    --grey-dark: #5e636a;
    --ink: #3a3f47;
    --faint: #e8ecf3;
  }
  * { margin: 0; padding: 0; box-sizing: border-box; }
  html, body { width: 1200px; height: 343px; overflow: hidden; }
  body { background: var(--bg); font-family: "Open Sans", Arial, sans-serif; color: var(--ink); position: relative; }

  .piece { position: absolute; background: var(--paper); box-shadow: 0 2px 6px rgba(0,0,0,.18); overflow: hidden; }
  .wave { position: absolute; left: 0; width: 100%; display: block; }

  .lockup { display: flex; align-items: center; gap: 3px; color: var(--navy); font-weight: 700; line-height: 1.15; }
  .lockup .dot { width: 7px; height: 7px; border-radius: 50%; background: var(--blue); flex: none; }
  .lockup .name { font-size: 6px; white-space: nowrap; }
  .lockup.stacked { flex-direction: column; align-items: flex-start; gap: 2px; }
  .lockup.stacked .name { white-space: normal; }
  .lockup.large .dot { width: 14px; height: 14px; }
  .lockup.large .name { font-size: 11px; }
  .lockup.on-blue { color: #fff; }
  .lockup.on-blue .dot { background: #fff; }

  .faint-mark { position: absolute; color: var(--faint); font-weight: 700; font-size: 22px; text-align: center; line-height: 1.1; }

  /* business cards */
  .card { width: 144px; height: 84px; left: 12px; }
  .card-front { top: 30px; }
  .card-back { top: 140px; background: linear-gradient(135deg, var(--blue) 0%, var(--navy) 100%); }
  .card-alt { top: 250px; }
  .card-front .lockup { position: absolute; left: 6px; top: 7px; width: 58px; }
  .card-front .lockup .name { font-size: 4.6px; }
  .card-front .details { position: absolute; right: 6px; top: 7px; width: 72px; font-size: 4px; line-height: 1.45; text-align: right; }
  .card-front .details .person { font-weight: 700; color: var(--navy); font-size: 4.6px; white-space: nowrap; }
  .card-back .lockup, .card-alt .lockup { position: absolute; left: 0; right: 0; top: 34px; justify-content: center; }
  .card-alt .url { position: absolute; left: 6px; bottom: 5px; font-size: 4px; color: var(--navy); }

  /* letterheads */
  .letterhead { width: 221px; height: 316px; top: 16px; }
  .lh-one { left: 166px; }
  .lh-two { left: 404px; }
  .letterhead .lockup { position: absolute; left: 0; right: 0; top: 10px; justify-content: center; }
  .letterhead .faint-mark { left: 20px; right: 20px; top: 110px; }
  .letterhead .footer { position: absolute; left: 0; right: 0; bottom: 6px; font-size: 4px; color: #fff; text-align: center; }

  /* envelopes */
  .envelope { width: 240px; height: 112px; left: 638px; }
  .env-front-a { top: 88px; }
  .env-front-b { top: 220px; }
  .envelope .return { position: absolute; left: 10px; top: 10px; }
  .envelope .return .addr { font-size: 4px; margin-top: 3px; line-height: 1.4; }

  .env-back { width: 300px; height: 112px; left: 890px; }
  .eb-grey { top: 60px; background: #f4f4f4; }
  .eb-blue { top: 150px; left: 905px; width: 285px; background: linear-gradient(90deg, var(--blue) 0%, var(--navy) 100%); }
  .eb-white { top: 225px; height: 110px; }
  .env-back .lockup { position: absolute; left: 0; right: 0; top: 20px; justify-content: center; }
  .env-back .flap { position: absolute; left: 0; top: 0; width: 100%; height: 100%; }
</style>
</head>
<body>
<svg width="0" height="0" style="position:absolute" aria-hidden="true">
  <defs>
    <linearGradient id="bandGrad" x1="0" x2="1" y1="0" y2="0">
      <stop offset="0" stop-color="#2c5fb3"/>
      <stop offset="1" stop-color="#1b3a7a"/>
    </linearGradient>
  </defs>
</svg>

<!-- Business card: front -->
<section class="piece card card-front">
  <div class="lockup stacked"><span class="dot"></span><span class="name">Hargrove Orthopedics and Sports Medicine</span></div>
  <div class="details">
    <div class="person">Daniel K. Hargrove Jr., M.D.</div>
    <div>Orthopedic Surgeon</div>
    <div>418 North Pelham Street</div>
    <div>Lowell, AR 72819</div>
    <div>Tel 479 555 0142</div>
    <div>Fax 479 555 0143</div>
    <div>hargrovemd.com</div>
    <div>fb.com/hargrovemd</div>
  </div>
  <svg class="wave" style="bottom:0;height:12px" viewBox="0 0 144 12" preserveAspectRatio="none">
    <path d="M0 7 Q72 0 144 4 L144 12 L0 12Z" fill="url(#bandGrad)"/>
  </svg>
</section>

<!-- Business card: back -->
<section class="piece card card-back">
  <div class="lockup large on-blue"><span class="dot"></span><span class="name">Hargrove</span></div>
</section>

<!-- Business card: alternate -->
<section class="piece card card-alt">
  <div class="lockup large"><span class="dot"></span><span class="name">Hargrove</span></div>
  <div class="url">hargrovemd.com</div>
</section>

<!-- Letterheads -->
<section class="piece letterhead lh-one">
  <div class="lockup"><span class="dot"></span><span class="name">Hargrove Orthopedics and Sports Medicine</span></div>
  <div class="faint-mark">Hargrove</div>
  <svg class="wave" style="bottom:0;height:34px" viewBox="0 0 221 34" preserveAspectRatio="none">
    <path d="M0 8 Q110 30 221 10 L221 34 L0 34Z" fill="url(#bandGrad)"/>
    <path d="M0 4 Q110 26 221 6" stroke="#9fb4d9" stroke-width="1.2" fill="none"/>
  </svg>
  <div class="footer">418 North Pelham Street · Lowell, AR 72819 · hargrovemd.com</div>
</section>

<section class="piece letterhead lh-two">
  <div class="lockup"><span class="dot"></span><span class="name">Hargrove Orthopedics and Sports Medicine</span></div>
  <div class="faint-mark">Hargrove</div>
  <svg class="wave" style="bottom:0;height:34px" viewBox="0 0 221 34" preserveAspectRatio="none">
    <path d="M0 8 Q110 30 221 10 L221 34 L0 34Z" fill="url(#bandGrad)"/>
    <path d="M0 4 Q110 26 221 6" stroke="#9fb4d9" stroke-width="1.2" fill="none"/>
  </svg>
  <div class="footer">418 North Pelham Street · Lowell, AR 72819 · hargrovemd.com</div>
</section>

<!-- Envelope fronts -->
<section class="piece envelope env-front-a">
  <div class="return">
    <div class="lockup"><span class="dot"></span><span class="name">Hargrove Orthopedics and Sports Medicine</span></div>
    <div class="addr">418 North Pelham Street<br>Lowell, AR 72819</div>
  </div>
  <svg class="wave" style="bottom:0;height:30px" viewBox="0 0 240 30" preserveAspectRatio="none">
    <path d="M0 18 Q120 -2 240 14 L240 30 L0 30Z" fill="url(#bandGrad)"/>
    <path d="M0 14 Q120 -6 240 10" stroke="#9fb4d9" stroke-width="1" fill="none"/>
  </svg>
</section>

<section class="piece envelope env-front-b">
  <div class="return">
    <div class="lockup"><span class="dot"></span><span class="name">Hargrove Orthopedics and Sports Medicine</span></div>
    <div class="addr">418 North Pelham Street<br>Lowell, AR 72819</div>
  </div>
  <svg class="wave" style="bottom:0;height:30px" viewBox="0 0 240 30" preserveAspectRatio="none">
    <path d="M0 18 Q120 -2 240 14 L240 30 L0 30Z" fill="url(#bandGrad)"/>
    <path d="M0 14 Q120 -6 240 10" stroke="#9fb4d9" stroke-width="1" fill="none"/>
  </svg>
</section>

<!-- Envelope backs -->
<section class="piece env-back eb-grey">
  <svg class="flap" viewBox="0 0 300 112" preserveAspectRatio="none">
    <path d="M0 0 L300 0 L300 30 L150 58 L0 30Z" fill="var(--grey-flap)"/>
    <path d="M0 30 L150 58 L300 30" stroke="var(--grey-dark)" stroke-width="1" fill="none"/>
  </svg>
  <div class="lockup on-blue"><span class="dot"></span><span class="name">Hargrove</span></div>
</section>

<section class="piece env-back eb-blue">
  <svg class="flap" viewBox="0 0 285 112" preserveAspectRatio="none">
    <path d="M0 0 L285 0 L142 50Z" fill="#1a356f"/>
  </svg>
</section>

<section class="piece env-back eb-white">
  <svg class="flap" viewBox="0 0 300 110" preserveAspectRatio="none">
    <path d="M0 0 L150 52 L300 0" stroke="#c9ccd1" stroke-width="1" fill="none"/>
    <path d="M0 110 L120 56 M300 110 L180 56" stroke="#dcdfe3" stroke-width="1" fill="none"/>
  </svg>
  <div class="lockup"><span class="dot"></span><span class="name">Hargrove</span></div>
</section>
</body>
</html>
```